Solar Energy Company Overview Presentation

Hello designers,

Our company Vantrel Energy Solutions is looking to re-design our company overview presentation labeled "Statement of Qualifications". Currently this document is provided in .doc and .PDF formats to clients and partners.

We would like to keep a professional and clean look, while making it look more sleek and up to do date with more modern design standards. Please see attached document for the current layout.

In addition we would like to add a page for corporate leadership, that is not currently on the document. It will have a photo of team member, title, and bio.

This should be a template that can be edited in the future with Microsoft word if possible. We also have the capabilities to use Photoshop if needed.

I have attached our current document titled "Statement of Qualifications" so you can view the type of content that is on it. I also attached other marketing items so you can get an idea of how some of our other branding looks. I have also attached the font we like to use. Please feel free to take you own creative direction.

Our website is http://vantrelenergy-example.com

Thank you for your consideration, please message me with any questions.

Galen

Target Market(s)

Solar Industry Companies and Clients

Industry/Entity Type

It Company

Requirements
Must have
• Professional Design With Modern High-End Look

```html
<!DOCTYPE html>
<html lang="en">
<head>
<meta charset="utf-8">
<title>Vantrel Energy Solutions – Statement of Qualifications</title>
<link href="https://fonts.googleapis.com/css2?family=Montserrat:wght@500;600;700;800&family=Raleway:wght@400;500;600&display=swap" rel="stylesheet">
<style>
:root{
  --orange:#f26b1d;
  --orange-dark:#e0571a;
  --orange-light:#f79a5c;
  --ink:#2b2b2b;
  --charcoal:#3a3839;
  --grey:#6b6b6b;
  --rule:#c9c9c9;
  --paper:#ffffff;
  --bg:#e8e5e1;
}
*{margin:0;padding:0;box-sizing:border-box}
html,body{width:1200px;height:1114px;overflow:hidden;background:var(--bg)}
body{position:relative;font-family:"Raleway",sans-serif;color:var(--ink)}
.page{position:absolute;width:357px;height:507px;background:var(--paper);overflow:hidden;box-shadow:0 4px 14px rgba(0,0,0,.25)}
.page--intro{left:229px;top:39px}
.page--cover{left:614px;top:39px}
.page--facilities{left:37px;top:569px}
.page--leadership{left:421px;top:569px}
.page--development{left:805px;top:569px}
.abs{position:absolute}
.page-head{position:absolute;left:32px;right:32px;top:24px;height:12px;display:flex;align-items:center;gap:6px;font-family:"Montserrat",sans-serif;font-size:6px}
.page-head .rule{flex:1;height:1px;background:linear-gradient(90deg,var(--orange) 0 25%,var(--ink) 25%)}
.page-head .brand{font-weight:700;font-size:6px;color:var(--ink);white-space:nowrap}
h2{font-family:"Montserrat",sans-serif;font-weight:800;color:var(--orange);font-size:12px;text-align:center;letter-spacing:.2px}
h2::after{content:"";display:block;width:34px;height:2px;background:var(--ink);margin:4px auto 0}
h3{font-family:"Montserrat",sans-serif;font-weight:700;color:var(--orange);font-size:10px}
.body-text{font-size:6.2px;line-height:1.4;text-align:justify;color:var(--ink)}
.body-text p+p{margin-top:7px}
.photo{position:absolute;border-radius:50%;border:3px solid var(--orange)}
/* cover */
.cover-brand{position:absolute;left:150px;top:52px;background:#fff;padding:6px 14px;font-family:"Montserrat",sans-serif;font-weight:800;font-size:24px;color:var(--ink);white-space:nowrap}
.cover-title{position:absolute;left:228px;top:332px;font-family:"Montserrat",sans-serif;font-weight:800;font-size:11.5px;line-height:1.25;color:#fff}
.cover-title .accent{color:var(--orange)}
.contact{position:absolute;left:26px;top:418px;font-family:"Montserrat",sans-serif;font-weight:700;font-size:7.5px;color:var(--ink)}
.contact li{list-style:none;display:flex;gap:8px;align-items:flex-start;margin-bottom:6px;line-height:1.35}
.contact svg{flex:none;margin-top:1px}
/* facilities */
.facility{position:absolute;left:0;width:357px;height:113px}
.facility .band{position:absolute;left:91px;right:0;top:0;bottom:0;background:var(--orange)}
.facility .photo{left:23px;top:-8px;width:128px;height:128px;background:radial-gradient(circle at 40% 40%,#b9b3a7,#6f6a62)}
.facility .photo.canopy{background:linear-gradient(160deg,#e8ecef,#8c9aa6 55%,#6a7b5e)}
.facility h4{position:absolute;left:165px;top:14px;font-family:"Montserrat",sans-serif;font-weight:600;font-size:9px;color:var(--ink);white-space:nowrap}
.facility dl{position:absolute;left:165px;top:28px;width:176px;font-size:5.2px;color:#fff}
.facility .row{display:flex;border-bottom:1px solid rgba(255,255,255,.35);padding:2px 0;line-height:1.25}
.facility dt{width:88px}
/* leadership */
.member{position:absolute;width:92px;text-align:center}
.member .photo{position:relative;margin:0 auto;width:74px;height:74px;background:linear-gradient(180deg,#d9d9d9,#f4f4f4)}
.member .title{font-family:"Montserrat",sans-serif;font-weight:600;color:var(--orange);font-size:7.2px;margin-top:6px}
.member .designation{font-family:"Montserrat",sans-serif;font-weight:700;font-size:6px;padding-bottom:3px;border-bottom:1px solid var(--rule)}
.member .bio{font-size:6.2px;line-height:1.4;text-align:left;margin-top:3px}
.connector{position:absolute;height:20px;background:var(--orange)}
/* development */
.dev-brand{position:absolute;left:33px;top:58px;font-family:"Montserrat",sans-serif;font-weight:800;font-size:15px;color:var(--ink);white-space:nowrap}
.node{position:absolute;border-radius:50%;display:flex;align-items:center;justify-content:center}
.node--orange{background:var(--orange)}
.node--dark{background:#1f1f1f}
.node-label{position:absolute;font-size:6.3px;line-height:1.3;color:var(--ink)}
</style>
</head>
<body>

<section class="page page--intro">
  <div class="page-head"><span>04</span><span class="rule"></span><span class="brand">Vantrel Energy</span></div>
  <svg class="abs" style="left:0;top:60px" width="357" height="100" viewBox="0 0 357 100" aria-hidden="true">
    <polygon points="0,26 140,0 220,0 0,80" fill="var(--orange)"/>
    <polygon points="0,26 60,15 30,60 0,80" fill="var(--orange-dark)"/>
  </svg>
  <div class="photo" role="img" aria-label="Photo of power transmission towers above solar panels" style="left:85px;top:51px;width:190px;height:190px;background:linear-gradient(160deg,#eef1f4 0 50%,#9aa6b2 60%,#3e4f66)"></div>
  <h2 class="abs" style="left:0;right:0;top:253px">INTRODUCTION</h2>
  <div class="body-text abs" style="left:32px;right:32px;top:283px">
    <p>Vantrel Energy Solutions and the Vantrel Group, family of companies, provide renewable energy solutions and services. We specialize in developing, financing, constructing, owning and operating solar and wind energy generation facilities. Facilities which range from small distributed generation to utility scale projects located across North America and the Pacific Islands. At Vantrel Energy Solutions, we believe in creating power from sustainable, clean resources that will benefit our communities.</p>
    <p>With the global push towards cleaner and more efficient ways of producing electricity, Vantrel Energy Solutions has come to the forefront of the industry to lead the charge. Our company's experience, innovative approach, business partners, and sponsorship have caused a growth that can only be measured by leaps and bounds.</p>
    <p>With segregations in the market, the founding members of Vantrel Energy Solutions saw a need to create a conglomerate. By affectively bringing all of the parties involved in a renewable energy project under one umbrella, Vantrel Energy Solutions can take a project from its inception to operation in the most efficient approach possible.</p>
  </div>
  <h3 class="abs" style="left:32px;top:430px">EXPERTISE</h3>
  <div class="body-text abs" style="left:32px;right:32px;top:443px">
    <p>The founding members of Vantrel Energy Solutions have over 40 combined years in the industry. In that time, our record has been flawless in bringing projects to fruition. Our employees are specialty-trained for the benefit of our clients and those looking to benefit from clean energy. We are focused on value, safety, and sustainability.</p>
  </div>
</section>

<section class="page page--cover">
  <svg class="abs" style="left:0;top:0" width="357" height="507" viewBox="0 0 357 507">
    <defs>
      <linearGradient id="field" x1="0" y1="0" x2="0" y2="1">
        <stop offset="0" stop-color="#b6a893"/>
        <stop offset=".35" stop-color="#3c4f73"/>
        <stop offset="1" stop-color="#28385a"/>
      </linearGradient>
    </defs>
    <g role="img" aria-label="Aerial photo of a large ground-mounted solar farm">
      <polygon points="0,0 357,0 357,60 0,60" fill="#a9bccb"/>
      <polygon points="0,60 357,60 357,215 178,335 0,244" fill="url(#field)"/>
    </g>
    <polygon points="0,244 178,335 0,270" fill="var(--orange)"/>
    <polygon points="0,244 90,290 40,300 0,270" fill="var(--orange-dark)"/>
    <polygon points="90,290 178,335 130,390 60,340" fill="var(--orange-light)"/>
    <polygon points="60,340 130,390 178,335 190,400" fill="var(--orange)"/>
    <polygon points="178,335 357,215 357,445 190,400" fill="var(--charcoal)"/>
  </svg>
  <div class="cover-brand">Vantrel Energy</div>
  <div class="cover-title"><span class="accent">[STATEMENT OF</span><br>QUALIFICATIONS]</div>
  <ul class="contact">
    <li><svg width="10" height="10" viewBox="0 0 10 10"><circle cx="5" cy="5" r="5" fill="var(--orange)"/><circle cx="5" cy="4.2" r="1.6" fill="#fff"/></svg><span>410 MERIDIAN PLAZA<br>SUITE 1200<br>AUSTIN, TEXAS 78701</span></li>
    <li><svg width="10" height="10" viewBox="0 0 10 10"><circle cx="5" cy="5" r="5" fill="var(--orange)"/><path d="M3 3l1.2-.3.6 1.4-.7.6a4 4 0 0 0 1.8 1.8l.6-.7 1.4.6L7.6 7.6A4.6 4.6 0 0 1 3 3z" fill="#fff"/></svg><span>555.014.2760</span></li>
    <li><svg width="10" height="10" viewBox="0 0 10 10"><circle cx="5" cy="5" r="5" fill="var(--orange)"/><circle cx="5" cy="5" r="2.6" fill="none" stroke="#fff" stroke-width=".8"/></svg><span>WWW.VANTRELENERGY-EXAMPLE.COM</span></li>
  </ul>
</section>

<section class="page page--facilities">
  <div class="page-head"><span>04</span><span class="rule"></span><span class="brand">Vantrel Energy</span></div>
  <h2 class="abs" style="left:0;right:0;top:51px">COMPLETED SOLAR FACILITIES</h2>

  <article class="facility" style="top:91px">
    <div class="band"></div>
    <div class="photo" role="img" aria-label="Aerial photo of the temple parking canopy system"></div>
    <h4>COMMUNITY TEMPLE</h4>
    <dl>
      <div class="row"><dt>System Size (kWp rating):</dt><dd>80 kW</dd></div>
      <div class="row"><dt>Client:</dt><dd>Riverside Community Trust</dd></div>
      <div class="row"><dt>Location:</dt><dd>Glendale, AZ</dd></div>
      <div class="row"><dt>Commercial Operation Date:</dt><dd>March 1, 2013</dd></div>
      <div class="row"><dt>Current Status:</dt><dd>Operating</dd></div>
      <div class="row"><dt>Role(s):</dt><dd>Developer, EPC, PPA</dd></div>
      <div class="row"><dt>Type of System:</dt><dd>Parking Canopy System</dd></div>
    </dl>
  </article>

  <article class="facility" style="top:233px">
    <div class="band"></div>
    <div class="photo canopy" role="img" aria-label="Photo beneath a solar parking canopy"></div>
    <h4>DESERT MARKET STOP</h4>
    <dl>
      <div class="row"><dt>System Size (kWp rating):</dt><dd>80 kW</dd></div>
      <div class="row"><dt>Client:</dt><dd>Riverside Community Trust</dd></div>
      <div class="row"><dt>Location:</dt><dd>Glendale, AZ</dd></div>
      <div class="row"><dt>Commercial Operation Date:</dt><dd>March 1, 2013</dd></div>
      <div class="row"><dt>Current Status:</dt><dd>Operating</dd></div>
      <div class="row"><dt>Role(s):</dt><dd>Developer, EPC, PPA</dd></div>
      <div class="row"><dt>Type of System:</dt><dd>Parking Canopy System</dd></div>
    </dl>
  </article>

  <article class="facility" style="top:375px">
    <div class="band"></div>
    <div class="photo" role="img" aria-label="Aerial photo of the landfill solar park"></div>
    <h4>MESA RIDGE LANDFILL SOLAR PARK</h4>
    <dl>
      <div class="row"><dt>System Size (kWp rating):</dt><dd>80 kW</dd></div>
      <div class="row"><dt>Client:</dt><dd>Riverside Community Trust</dd></div>
      <div class="row"><dt>Location:</dt><dd>Glendale, AZ</dd></div>
      <div class="row"><dt>Commercial Operation Date:</dt><dd>March 1, 2013</dd></div>
      <div class="row"><dt>Current Status:</dt><dd>Operating</dd></div>
      <div class="row"><dt>Role(s):</dt><dd>Developer, EPC, PPA</dd></div>
      <div class="row"><dt>Type of System:</dt><dd>Parking Canopy System</dd></div>
    </dl>
  </article>
</section>

<section class="page page--leadership">
  <div class="page-head"><span>04</span><span class="rule"></span><span class="brand">Vantrel Energy</span></div>
  <h2 class="abs" style="left:0;right:0;top:56px">CORPORATE LEADERSHIP</h2>
  <div class="body-text abs" style="left:32px;right:32px;top:77px">
    <p>Vantrel Energy Solutions and the Vantrel Group, family of companies, provide renewable energy solutions and services. We specialize in developing, financing, constructing, owning and operating solar and wind energy generation facilities. Facilities which range from small distributed generation to utility scale projects located across North America and the Pacific Islands. At Vantrel Energy Solutions, we believe in creating power from sustainable, clean resources that will benefit our communities.</p>
  </div>

  <div class="connector" style="left:60px;width:240px;top:173px"></div>
  <div class="connector" style="left:60px;width:240px;top:343px"></div>

  <div class="member" style="left:32px;top:146px"><div class="photo" role="img" aria-label="Team member portrait"></div><div class="title">Team Member Title</div><div class="designation">Designation</div><p class="bio">Vantrel Energy Solutions and the Vantrel Group, family of companies, provide renewable energy solutions and services. We specialize in developing.</p></div>
  <div class="member" style="left:133px;top:146px"><div class="photo" role="img" aria-label="Team member portrait"></div><div class="title">Team Member Title</div><div class="designation">Designation</div><p class="bio">Vantrel Energy Solutions and the Vantrel Group, family of companies, provide renewable energy solutions and services. We specialize in developing.</p></div>
  <div class="member" style="left:234px;top:146px"><div class="photo" role="img" aria-label="Team member portrait"></div><div class="title">Team Member Title</div><div class="designation">Designation</div><p class="bio">Vantrel Energy Solutions and the Vantrel Group, family of companies, provide renewable energy solutions and services. We specialize in developing.</p></div>
  <div class="member" style="left:32px;top:316px"><div class="photo" role="img" aria-label="Team member portrait"></div><div class="title">Team Member Title</div><div class="designation">Designation</div><p class="bio">Vantrel Energy Solutions and the Vantrel Group, family of companies, provide renewable energy solutions and services. We specialize in developing.</p></div>
  <div class="member" style="left:133px;top:316px"><div class="photo" role="img" aria-label="Team member portrait"></div><div class="title">Team Member Title</div><div class="designation">Designation</div><p class="bio">Vantrel Energy Solutions and the Vantrel Group, family of companies, provide renewable energy solutions and services. We specialize in developing.</p></div>
  <div class="member" style="left:234px;top:316px"><div class="photo" role="img" aria-label="Team member portrait"></div><div class="title">Team Member Title</div><div class="designation">Designation</div><p class="bio">Vantrel Energy Solutions and the Vantrel Group, family of companies, provide renewable energy solutions and services. We specialize in developing.</p></div>
</section>

<section class="page page--development">
  <div class="page-head" style="right:150px"><span>04</span><span class="rule"></span></div>
  <svg class="abs" style="left:170px;top:0" width="187" height="180" viewBox="0 0 187 180">
    <polygon points="20,70 130,0 187,0 187,180" fill="var(--orange)"/>
    <polygon points="20,70 95,22 88,80" fill="var(--orange-dark)"/>
    <polygon points="88,80 187,150 187,180" fill="var(--orange-light)"/>
    <polygon points="98,70 187,25 187,120" fill="#8a8f96" role="img" aria-label="Photo of interlocking gears"/>
  </svg>
  <div class="dev-brand">Vantrel Energy</div>
  <h3 class="abs" style="left:33px;top:105px">PROJECT DEVELOPMENT</h3>
  <div class="body-text abs" style="left:33px;width:196px;top:118px">
    <p>Developing energy projects is where Vantrel Energy Solutions got its start. The experience that we have in this arena is very diverse. Whether it is developing our own projects or partnering with other developers for the benefit of their clients, Vantrel Energy Solutions has done it all. Crucial development services that we provide our clients and partners are:</p>
  </div>

  <svg class="abs" style="left:0;top:0" width="357" height="507" viewBox="0 0 357 507" aria-hidden="true">
    <circle cx="115" cy="320" r="66" fill="none" stroke="#dedede" stroke-width="2"/>
    <circle cx="245" cy="304" r="66" fill="none" stroke="#dedede" stroke-width="2"/>
  </svg>

  <div class="node node--dark" style="left:95px;top:232px;width:52px;height:52px"><svg width="22" height="22" viewBox="0 0 22 22"><rect x="3" y="3" width="16" height="11" fill="none" stroke="var(--orange)" stroke-width="1.6"/><path d="M6 11l3-3 3 2 4-4M8 14l-2 6M14 14l2 6" stroke="var(--orange)" stroke-width="1.6" fill="none"/></svg></div>
  <div class="node node--orange" style="left:178px;top:228px;width:42px;height:42px"><svg width="16" height="18" viewBox="0 0 16 18"><rect x="1" y="1" width="14" height="16" rx="1" fill="none" stroke="#1f1f1f" stroke-width="1.6"/><text x="8" y="13" text-anchor="middle" font-family="Montserrat,sans-serif" font-weight="700" font-size="10" fill="#1f1f1f">$</text></svg></div>
  <div class="node node--orange" style="left:269px;top:223px;width:50px;height:50px"><svg width="20" height="14" viewBox="0 0 20 14"><rect x="1" y="1" width="18" height="12" rx="1" fill="none" stroke="#1f1f1f" stroke-width="1.6"/><rect x="4" y="4" width="5" height="5" fill="#1f1f1f"/><path d="M11 5h5M11 8h5" stroke="#1f1f1f" stroke-width="1.4"/></svg></div>
  <div class="node node--orange" style="left:27px;top:309px;width:52px;height:52px"><svg width="22" height="20" viewBox="0 0 22 20"><rect x="3" y="12" width="3" height="6" fill="#1f1f1f"/><rect x="8" y="9" width="3" height="9" fill="#1f1f1f"/><rect x="13" y="6" width="3" height="12" fill="#1f1f1f"/><path d="M2 10l7-5 4 2 6-5" stroke="#1f1f1f" stroke-width="1.5" fill="none"/><path d="M1 19h20" stroke="#1f1f1f" stroke-width="1.4"/></svg></div>
  <div class="node node--dark" style="left:113px;top:364px;width:46px;height:46px"><svg width="20" height="20" viewBox="0 0 20 20"><circle cx="10" cy="10" r="7" fill="none" stroke="var(--orange)" stroke-width="1.4"/><circle cx="10" cy="10" r="2" fill="var(--orange)"/><path d="M10 3v14M3 10h14" stroke="var(--orange)" stroke-width="1"/></svg></div>
  <div class="node node--orange" style="left:194px;top:329px;width:52px;height:52px"><svg width="20" height="18" viewBox="0 0 20 18"><rect x="2" y="10" width="3" height="7" fill="#1f1f1f"/><rect x="7" y="8" width="3" height="9" fill="#1f1f1f"/><rect x="12" y="10" width="3" height="7" fill="#1f1f1f"/><path d="M4 6l4-4 4 3 4-3" stroke="#1f1f1f" stroke-width="1.6" fill="none"/></svg></div>
  <div class="node node--dark" style="left:288px;top:301px;width:44px;height:44px"><svg width="16" height="16" viewBox="0 0 16 16"><g stroke="var(--orange)" stroke-width="1.6" stroke-linecap="round"><path d="M8 1v3M8 12v3M1 8h3M12 8h3M3 3l2 2M11 11l2 2M13 3l-2 2M5 11l-2 2"/></g></svg></div>

  <span class="node-label" style="left:94px;top:209px">Determining<br>project feasibility</span>
  <span class="node-label" style="left:179px;top:197px">Conceptual budgets,<br>design and material<br>identification</span>
  <span class="node-label" style="left:269px;top:205px">Site identification<br>and site control</span>
  <span class="node-label" style="left:26px;top:371px">Financial<br>Modeling</span>
  <span class="node-label" style="left:112px;top:421px;text-align:center">Interconnection<br>process</span>
  <span class="node-label" style="left:193px;top:389px">PPA negotiations</span>
  <span class="node-label" style="left:288px;top:351px;text-align:center">Entitlement &amp;<br>the permitting<br>process</span>

  <div class="body-text abs" style="left:33px;right:32px;top:449px;text-align:left">
    <p>In many cases, Vantrel Energy Solutions assumes the role of a late stage developer; stepping into the developer role late in the development cycle of a project. Partnering with local developers or securing projects which are "shovel ready".</p>
  </div>
</section>

</body>
</html>
```